Vel-Trax.ch is looking for business card letterhead and envelope C5 with WOW effect

We need a strong business card for our company Vel-Trax.ch, logo is available. You want a black or dark background on which the logo Stark r% 26 # 252; appears. Letterhead and envelope in C5 format should be in a similar design, but does not have to be We need a strong business card for our company Vel-Trax.ch, logo is available. A black or dark background is desired, on which the logo Stark comes across. The letterhead and the envelope in C5 format should have a similar design.

Target Market(s)

Private customers as well as entrepreneurs

Contact Information for Business Card

E-mail: info@vel-trax.ch
Web.www.Vel-Trax.ch
Tel: +41 ( 0 ) 79 684 3027
Adresse:
Lindenhaldeweg 14
9403 Brenzikon

Hier kann man Icons verwenden für Email,Tel und Adressse

Font styles to use
Other font styles liked:
• Dubai,bold

Colors

Designer to choose colors to be used in the design.

Requirements
Must have
• WOW effect
Nice to have
• R% 26 # 252; back business card with our service listings. - VEHICLE LABELING - SHOP WINDOW LABELING - STICKERS AND MUCH MORE ... in red color

```html
<!DOCTYPE html>
<html lang="de">
<head>
<meta charset="utf-8">
<title>Vel-Trax.ch – Visitenkarte</title>
<link rel="stylesheet" href="https://fonts.googleapis.com/css2?family=Open+Sans:wght@400;600;700&display=swap">
<style>
  :root {
    --yellow: #f2c117;
    --yellow-soft: #f6d56a;
    --ink: #1c1c1c;
    --card-dark: #1f1f21;
    --text-light: #f4f4f4;
    --desk: #e4e1dc;
  }
  * { box-sizing: border-box; margin: 0; padding: 0; }
  html, body {
    width: 1200px; height: 843px; overflow: hidden;
    background: var(--desk);
    font-family: "Open Sans", Arial, sans-serif;
    color: var(--ink);
  }
  .sheet {
    width: 1200px; height: 843px;
    display: flex; align-items: center; justify-content: center; gap: 40px;
  }
  .card {
    position: relative;
    width: 540px; height: 320px;
    overflow: hidden;
    box-shadow: 0 6px 18px rgba(0,0,0,0.22);
  }

  /* Front side */
  .card-front { background: var(--card-dark); color: var(--text-light); }
  .accent-bar {
    position: absolute; left: 12px; top: 22px;
    width: 9px; height: 92px; background: var(--yellow);
  }
  .accent-mark {
    position: absolute; left: 12px; bottom: 22px;
    width: 9px; height: 30px; background: var(--text-light);
  }
  .contact-list {
    position: absolute; left: 46px; top: 22px;
    list-style: none; font-size: 14px; font-weight: 600; line-height: 24px;
  }
  .contact-list li { display: flex; align-items: center; gap: 12px; }
  .icon { width: 18px; height: 18px; flex: none; }
  .brand {
    position: absolute; left: 180px; top: 138px;
    display: flex; align-items: center; gap: 14px;
  }
  .brand-square { width: 34px; height: 34px; background: var(--yellow); }
  .brand-name {
    font-size: 32px; font-weight: 700; letter-spacing: 1px;
  }
  .address {
    position: absolute; left: 46px; bottom: 24px;
    display: flex; align-items: center; gap: 12px;
    font-size: 14px; font-weight: 600; line-height: 19px;
  }

  /* Back side */
  .card-back { background: var(--yellow); }
  .honeycomb-field {
    position: absolute; left: 0; top: 70px; width: 440px; height: 250px;
    background: radial-gradient(ellipse at 20% 75%, var(--yellow-soft) 0%, rgba(246,213,106,0.6) 40%, rgba(242,193,23,0) 75%);
  }
  .back-brand {
    position: absolute; right: 44px; top: 40px; text-align right;
    text-align: right; color: var(--ink);
  }
  .back-brand .brand-name { font-size: 38px; }
  .back-web {
    font-size: 14px; font-weight: 600; letter-spacing: 5px; margin-top: -2px;
  }
</style>
</head>
<body>
<main class="sheet">
  <section class="card card-front" aria-label="Visitenkarte Vorderseite">
    <span class="accent-bar"></span>
    <span class="accent-mark"></span>
    <ul class="contact-list">
      <li>
        <svg class="icon" viewBox="0 0 24 24" fill="none" stroke="#f2c117" stroke-width="1.6" stroke-linejoin="round"><path d="M5 3h4l2 5-2.5 1.5a11 11 0 0 0 6 6L16 13l5 2v4a2 2 0 0 1-2 2A16 16 0 0 1 3 5a2 2 0 0 1 2-2z"/></svg>
        +41 ( 0 ) 79 684 3027
      </li>
      <li>
        <svg class="icon" viewBox="0 0 24 24" fill="none" stroke="#f2c117" stroke-width="1.6"><rect x="3" y="6" width="18" height="12" rx="1"/><path d="M3 7l9 6 9-6"/></svg>
        info@vel-trax.ch
      </li>
      <li>
        <svg class="icon" viewBox="0 0 24 24" fill="none" stroke="#f2c117" stroke-width="1.6"><circle cx="12" cy="12" r="9"/><path d="M3 12h18M12 3c3 3 3 15 0 18M12 3c-3 3-3 15 0 18"/></svg>
        www.Vel-Trax.ch
      </li>
    </ul>
    <div class="brand">
      <span class="brand-square"></span>
      <span class="brand-name">VEL-TRAX.CH</span>
    </div>
    <div class="address">
      <svg class="icon" viewBox="0 0 24 24" fill="none" stroke="#f2c117" stroke-width="1.6"><path d="M12 21s-6-6.5-6-11a6 6 0 0 1 12 0c0 4.5-6 11-6 11z"/><circle cx="12" cy="10" r="2.2"/></svg>
      <p>Lindenhaldeweg 14<br>9403 Brenzikon</p>
    </div>
  </section>

  <section class="card card-back" aria-label="Visitenkarte Rückseite">
    <div class="honeycomb-field" role="img" aria-label="Dekoratives Wabenmuster in hellen Gelbtönen"></div>
    <div class="back-brand">
      <div class="brand-name">VEL-TRAX.CH</div>
      <div class="back-web">www.Vel-Trax.ch</div>
    </div>
  </section>
</main>
</body>
</html>
```